Bref créative
Design Business Card & Stationary
Talvix Studio
Professional
Derek Holt
4837 Birchwood Lane Suite #210
Harlow Bay, OR 97499
derek@talvixstudio.example
www.talvixstudio.example
This is our logo

```html
<!DOCTYPE html>
<html lang="en">
<head>
<meta charset="utf-8">
<title>Talvix Studio Business Card</title>
<link href="https://fonts.googleapis.com/css2?family=Cabin:wght@400;600;700&display=swap" rel="stylesheet">
<style>
  :root {
    --bg: #e9e7e3;
    --card: #ffffff;
    --ink: #3d3d3d;
    --ink-soft: #5a5a5a;
    --green: #6aa832;
    --green-light: #9fcf55;
    --green-dark: #1f4a2c;
    --divider: #bdbdbd;
  }
  * { margin: 0; padding: 0; box-sizing: border-box; }
  html, body { width: 1200px; height: 780px; overflow: hidden; }
  body {
    background: var(--bg);
    font-family: "Cabin", sans-serif;
    color: var(--ink);
  }
  .card {
    position: absolute;
    left: 80px;
    top: 93px;
    width: 1040px;
    height: 594px;
    background: var(--card);
    border-radius: 26px;
    overflow: hidden;
    box-shadow: 0 10px 30px rgba(0,0,0,0.18);
  }
  .brand {
    position: absolute;
    left: 190px;
    top: 100px;
    display: flex;
    align-items: center;
    gap: 22px;
  }
  .brand-mark {
    width: 72px;
    height: 72px;
    background: var(--green-dark);
    border-radius: 8px;
  }
  .brand-text { display: flex; flex-direction: column; }
  .brand-name {
    font-size: 72px;
    font-weight: 600;
    line-height: 1;
    color: var(--ink);
    letter-spacing: -1px;
  }
  .brand-tagline {
    font-size: 19px;
    color: var(--ink-soft);
    margin-top: 4px;
    padding-left: 8px;
    border-top: 1px solid var(--divider);
    padding-top: 3px;
    align-self: flex-end;
  }
  .person {
    position: absolute;
    right: 540px;
    top: 285px;
    text-align: right;
  }
  .person-name {
    font-size: 32px;
    font-weight: 700;
    color: var(--green);
    margin-bottom: 14px;
  }
  .person-address {
    font-size: 21px;
    line-height: 1.35;
    color: var(--ink);
  }
  .divider {
    position: absolute;
    left: 525px;
    top: 285px;
    width: 1px;
    height: 140px;
    background: var(--divider);
  }
  .contact-list {
    position: absolute;
    left: 545px;
    top: 283px;
    list-style: none;
  }
  .contact-item {
    display: flex;
    align-items: center;
    gap: 14px;
    font-size: 20px;
    line-height: 1;
    height: 30px;
    color: var(--ink);
  }
  .contact-icon { width: 18px; height: 18px; fill: var(--ink-soft); flex: none; }
  .swoosh { position: absolute; left: 0; bottom: 0; width: 1040px; height: 594px; }
</style>
</head>
<body>
  <div class="card">
    <svg class="swoosh" viewBox="0 0 1040 594" aria-hidden="true">
      <defs>
        <linearGradient id="bandGreen" x1="0" y1="0" x2="1" y2="0">
          <stop offset="0" stop-color="#9fcf55"/>
          <stop offset="1" stop-color="#6aa832"/>
        </linearGradient>
      </defs>
      <path d="M0,560 C320,540 700,510 1040,420 L1040,438 C700,530 320,560 0,578 Z" fill="var(--green-dark)"/>
      <path d="M0,594 L0,588 C320,570 720,545 1040,455 L1040,594 Z" fill="url(#bandGreen)"/>
    </svg>

    <div class="brand">
      <div class="brand-mark"></div>
      <div class="brand-text">
        <div class="brand-name">Talvix Studio</div>
        <div class="brand-tagline">Internet Presence Management</div>
      </div>
    </div>

    <div class="person">
      <div class="person-name">Derek Holt</div>
      <div class="person-address">4837 Birchwood Lane Suite #210<br>Harlow Bay, OR 97499</div>
    </div>

    <div class="divider"></div>

    <ul class="contact-list">
      <li class="contact-item">
        <svg class="contact-icon" viewBox="0 0 24 24"><path d="M6.6 10.8a15 15 0 0 0 6.6 6.6l2.2-2.2c.3-.3.7-.4 1-.2 1.1.4 2.3.6 3.6.6.6 0 1 .4 1 1V20c0 .6-.4 1-1 1A17 17 0 0 1 3 4c0-.6.4-1 1-1h3.5c.6 0 1 .4 1 1 0 1.3.2 2.5.6 3.6.1.3 0 .7-.2 1z"/></svg>
        <span>555-014-2281</span>
      </li>
      <li class="contact-item">
        <svg class="contact-icon" viewBox="0 0 24 24"><path d="M7 1h10a2 2 0 0 1 2 2v18a2 2 0 0 1-2 2H7a2 2 0 0 1-2-2V3a2 2 0 0 1 2-2zm0 3v14h10V4zm5 15.5a1.2 1.2 0 1 0 0 2.4 1.2 1.2 0 0 0 0-2.4z"/></svg>
        <span>555-016-7730</span>
      </li>
      <li class="contact-item">
        <svg class="contact-icon" viewBox="0 0 24 24"><path d="M2 5h20v14H2zm2 2v.4l8 5.2 8-5.2V7zm0 2.8V17h16V9.8l-8 5.2z"/></svg>
        <span>derek@talvixstudio.example</span>
      </li>
      <li class="contact-item">
        <svg class="contact-icon" viewBox="0 0 24 24"><path d="M12 2a10 10 0 1 0 0 20 10 10 0 0 0 0-20zm6.9 9h-3a15 15 0 0 0-1.3-5.6A8 8 0 0 1 18.9 11zM12 4.1c.9 1.2 1.8 3.6 1.9 6.9h-3.8c.1-3.3 1-5.7 1.9-6.9zM9.4 5.4A15 15 0 0 0 8.1 11h-3a8 8 0 0 1 4.3-5.6zM5.1 13h3a15 15 0 0 0 1.3 5.6A8 8 0 0 1 5.1 13zm6.9 6.9c-.9-1.2-1.8-3.6-1.9-6.9h3.8c-.1 3.3-1 5.7-1.9 6.9zm2.6-1.3a15 15 0 0 0 1.3-5.6h3a8 8 0 0 1-4.3 5.6z"/></svg>
        <span>www.talvixstudio.example</span>
      </li>
    </ul>
  </div>
</body>
</html>
```